Medical Company in need of Modern business card design for new Wound Care clinic.

Modern business card design for our Woundcare company. Logo and description of services can be found on our website; https://www.tovrel-woundcare.com/

```html
<!DOCTYPE html>
<html lang="en">
<head>
<meta charset="utf-8">
<title>Tovrel Woundcare – Business Card</title>
<link rel="stylesheet" href="https://fonts.googleapis.com/css2?family=Poppins:wght@300;400&family=Roboto:wght@400;500;700&display=swap">
<style>
  :root {
    --backdrop: #2a2a2a;
    --card-dark: #1f1f1f;
    --card-dark-2: #262626;
    --gold: #d9a94f;
    --gold-light: #e9bb63;
    --gold-deep: #b8873a;
    --text-light: #f2f2f2;
    --text-dark: #1a1a1a;
    --band: #d8d8d8;
  }
  * { margin: 0; padding: 0; box-sizing: border-box; }
  html, body { width: 1200px; height: 576px; overflow: hidden; }
  body { background: var(--backdrop); position: relative; font-family: 'Roboto', sans-serif; }

  .card {
    position: absolute; top: 138px; width: 484px; height: 294px;
    border-radius: 8px; overflow: hidden;
    background: linear-gradient(135deg, var(--card-dark-2), var(--card-dark));
    box-shadow: 0 4px 10px rgba(0,0,0,.45);
  }
  .card-front { left: 102px; }
  .card-back { left: 596px; }

  .front-name {
    position: absolute; left: 26px; top: 38px;
    font-family: 'Poppins', sans-serif; font-weight: 300;
    font-size: 22px; letter-spacing: 4px; color: var(--text-light);
  }
  .front-url {
    position: absolute; left: 26px; top: 243px;
    font-family: 'Poppins', sans-serif; font-weight: 300;
    font-size: 13px; color: var(--text-light);
  }

  .gold-panel { position: absolute; left: 0; top: 0; }
  .back-brand {
    position: absolute; left: 0; width: 234px; top: 168px; text-align: center;
    font-weight: 700; font-size: 18px; letter-spacing: .5px; color: var(--text-dark);
  }

  .holder { position: absolute; right: 29px; top: 30px; text-align: right; }
  .holder-name { font-weight: 700; font-size: 20px; color: var(--gold-light); line-height: 1.2; }
  .holder-title { font-size: 13px; color: var(--text-light); margin-top: 2px; }

  .address {
    position: absolute; right: 29px; top: 128px; text-align: right;
    font-size: 13px; line-height: 19px; color: var(--text-light);
  }
  .contacts {
    position: absolute; right: 29px; top: 171px; list-style: none;
    font-size: 13px; line-height: 19px; color: var(--text-light);
  }
  .contacts li { display: flex; justify-content: flex-end; align-items: center; gap: 8px; }
  .contacts svg { width: 11px; height: 11px; fill: var(--gold); }

  .services {
    position: absolute; left: 228px; right: 0; top: 253px; height: 23px;
    background: var(--band); color: var(--text-dark);
    font-size: 12.5px; line-height: 23px; padding-left: 24px;
  }
</style>
</head>
<body>
  <section class="card card-front">
    <h1 class="front-name">TOVREL WOUNDCARE</h1>
    <p class="front-url">tovrel-woundcare.com</p>
  </section>

  <section class="card card-back">
    <svg class="gold-panel" width="260" height="294" viewBox="0 0 260 294">
      <defs>
        <linearGradient id="goldFill" x1="0" y1="0" x2="0" y2="1">
          <stop offset="0" stop-color="#e8b862"/>
          <stop offset=".55" stop-color="#d4a14d"/>
          <stop offset="1" stop-color="#b48437"/>
        </linearGradient>
      </defs>
      <path d="M0 0 H214 Q260 147 218 294 H0 Z" fill="#c99845"/>
      <path d="M0 0 H206 Q252 147 210 294 H0 Z" fill="url(#goldFill)"/>
    </svg>
    <p class="back-brand">TOVREL WOUNDCARE</p>

    <div class="holder">
      <h2 class="holder-name">Dr. Mara Tovrel</h2>
      <p class="holder-title">Managing Director</p>
    </div>

    <address class="address" style="font-style:normal">
      2180 Linden Ave Ste 200 PMB<br>418207 Dallas, TX 75204
    </address>

    <ul class="contacts">
      <li>972-555-0148
        <svg viewBox="0 0 12 12"><path d="M1 4 Q6 0 11 4 L10 5.5 L8 5 L8 4 Q6 3 4 4 L4 5 L2 5.5 Z M3 6 H9 L10 11 H2 Z"/></svg>
      </li>
      <li>info@tovrel-woundcare.com
        <svg viewBox="0 0 12 12"><path d="M0 2 H12 V10 H0 Z M1 3 L6 7 L11 3" stroke="#1f1f1f" stroke-width=".8"/></svg>
      </li>
      <li>www.tovrel-woundcare.com
        <svg viewBox="0 0 12 12"><circle cx="6" cy="6" r="5.5"/><path d="M0.5 6 H11.5 M6 .5 V11.5 M2 3 H10 M2 9 H10" stroke="#1f1f1f" stroke-width=".7" fill="none"/></svg>
      </li>
    </ul>

    <p class="services">All type of Wound Treatment &amp; HBO</p>
  </section>
</body>
</html>
```